Quillon Maison Wood Fired Pizza business card design

I have a logo and need an eye catching design that will get me noticed.
My business is wood fired pizza. I want a bold design that will make our customers remember us and the food that we serve. Work with the colors of our logo and texts. Maybe add designs that lend to what or how pizza is made using our wood fired oven?

Target Market(s)

Foodies!

Contact Information for Business Card

Quillon Maison Wood Fired Pizza
Our slogan is Fast. Fresh. Handcrafted
Catering for all events

Requirements
Must have
• Dana Porrick
Telephone 570 555 0183
website www.getquillon.example
Facebook @getquillonpizza maybe use the facebook logo next to it
Instagram getquillonpizza maybe use the instagram logo next to it
Catering for all events
Nice to have
• Maybe pizza peels, pizza cutters? Wood? Fired wood? Using our flame in the background?
Please work with different colored text so each sentence stands out? A themed color for facebook?
Maybe work with the colors within our logo?
Please try to use the our quillon font, but not a must have.

```html
<!DOCTYPE html>
<html lang="en">
<head>
<meta charset="utf-8">
<title>Quillon Maison Wood Fired Pizza – Business Card</title>
<link rel="stylesheet" href="https://fonts.googleapis.com/css2?family=Krona+One&family=Poppins:wght@400;500&display=swap">
<style>
  :root {
    --page: #e9e6e2;
    --card: #111620;
    --red: #c91f28;
    --orange: #e8891c;
    --white: #ffffff;
    --display: "Krona One", sans-serif;
    --body: "Poppins", sans-serif;
  }
  * { box-sizing: border-box; margin: 0; padding: 0; }
  html, body { width: 1200px; height: 900px; overflow: hidden; }
  body {
    background: var(--page);
    display: flex;
    flex-direction: column;
    align-items: center;
    justify-content: center;
    gap: 40px;
  }
  .card {
    width: 700px;
    height: 400px;
    background: var(--card);
    display: flex;
    align-items: center;
    padding: 0 56px;
    box-shadow: 0 6px 18px rgba(0,0,0,.18);
  }
  .brand {
    width: 250px;
    flex: none;
    display: flex;
    flex-direction: column;
    align-items: center;
    gap: 14px;
  }
  .brand-mark {
    width: 92px;
    height: 92px;
    border-radius: 50%;
    background: var(--red);
  }
  .brand-name {
    font-family: var(--display);
    color: var(--white);
    font-size: 20px;
    letter-spacing: 2px;
    text-transform: uppercase;
    text-align: center;
    line-height: 1.35;
  }
  .brand-rule {
    width: 200px;
    height: 3px;
    background: var(--orange);
  }
  .slogan {
    font-family: var(--display);
    color: var(--white);
    font-size: 33px;
    line-height: 1.35;
    padding-left: 24px;
  }
  .details { padding-left: 24px; }
  .owner {
    font-family: var(--display);
    color: var(--red);
    font-size: 30px;
    line-height: 1.2;
    margin-bottom: 34px;
  }
  .contact-list { list-style: none; display: flex; flex-direction: column; gap: 14px; }
  .contact-item {
    display: flex;
    align-items: center;
    gap: 16px;
    font-family: var(--body);
    color: var(--white);
    font-size: 20px;
  }
  .contact-icon {
    width: 28px;
    height: 28px;
    border-radius: 4px;
    background: var(--red);
    flex: none;
    display: flex;
    align-items: center;
    justify-content: center;
  }
</style>
</head>
<body>

<section class="card card-front">
  <div class="brand">
    <div class="brand-mark"></div>
    <div class="brand-rule"></div>
    <div class="brand-name">Quillon Maison</div>
  </div>
  <p class="slogan">Fast.<br>Fresh.<br>Handcrafted</p>
</section>

<section class="card card-back">
  <div class="brand">
    <div class="brand-mark"></div>
    <div class="brand-rule"></div>
    <div class="brand-name">Quillon Maison</div>
  </div>
  <div class="details">
    <h1 class="owner">Dana and Lise<br>Porrick</h1>
    <ul class="contact-list">
      <li class="contact-item">
        <span class="contact-icon">
          <svg width="16" height="16" viewBox="0 0 24 24" aria-hidden="true"><path fill="#fff" d="M6.6 10.8a15.1 15.1 0 0 0 6.6 6.6l2.2-2.2a1 1 0 0 1 1-.25 11.4 11.4 0 0 0 3.6.57 1 1 0 0 1 1 1V20a1 1 0 0 1-1 1A17 17 0 0 1 3 4a1 1 0 0 1 1-1h3.5a1 1 0 0 1 1 1c0 1.25.2 2.45.57 3.6a1 1 0 0 1-.25 1z"/></svg>
        </span>570 555 0183
      </li>
      <li class="contact-item">
        <span class="contact-icon">
          <svg width="18" height="18" viewBox="0 0 24 24" aria-hidden="true" fill="none" stroke="#fff" stroke-width="1.8"><circle cx="12" cy="12" r="9"/><ellipse cx="12" cy="12" rx="4" ry="9"/><path d="M3 12h18M5 7h14M5 17h14"/></svg>
        </span>www.getquillon.example
      </li>
      <li class="contact-item"><span class="contact-icon"></span>@getquillonpizza</li>
      <li class="contact-item"><span class="contact-icon"></span>getquillonpizza</li>
    </ul>
  </div>
</section>

</body>
</html>
```